Macadamia Nuts Doypack Design

Brindlecove grows, processes and trades macadamia nuts globally (www.brindlecove.com). We mainly supply the nuts to packaging factories, who does final packaging for retailers. However we want to re-enter the retail market (which we have previously been active in) by offering macadamia nuts in shell within plastic pouch (“doypack”) – BUT we will also include a nice handcracker for free. Macadamia nuts are difficult to crack, and therefore a very special and rare aluminium cracker has been designed. This is a unique offering –nice twist on well known product.
To this end we are looking for a new or refreshed design of our previous retail range. This will be offered to the market during a trade show in Paris in 18-23 October 2014
WE ADDED AN OLD DESIGN - DONT JUST AMEND THE ELEMENTS AND GIVE IT BACK. THIS IS ONLY TO SHOW YOU SOME OF THE LEGAL REQUIREMENTS on retail packaging. We want a much better design than this.
Updates

Dear designers: 3 things to note: - please have a cutout (window) on the front of the pack where the macadamia nuts (product in bag) is visible. This window is essential because the product we offer is unique in that it is unusual to sell it in shell. Consumers need to see it. - We need the window large enough to make the free hand cracker visible (around 20-25% of the front view). - It emerged that the macadamia in shell picture with leaves used non-macadamia leaves. Therefore please don't use that image. I will upload other images of the product in shell. Thanks Anton

Hi all, thank you for the designs, our office will now create a final shortlist and revert back to you. Anton

Target Market(s)

Middle income health conscious buyers looking for a special snack product. It can also be used as a gift (e.g. airport duty free shops).

Industry/Entity Type

Legal

Font styles to use
Sans Serif

Colors
cadf82
faf289
faee3f
add136
f6faec
e9f1ce
fdf9cf
fee18a
9bcb3c

Requirements
Must have
• Comply with legal packaging requirements as per the attached briefing document (see sec ion on mandatory elements
Reference to the free nut cracker (see attached picture of steel photo)
Should not have
• Old style "farmhouse" design

```html
<!DOCTYPE html>
<html lang="en">
<head>
<meta charset="utf-8">
<title>Brindlecove Macadamia Nuts Doypack</title>
<link href="https://fonts.googleapis.com/css2?family=Source+Sans+3:wght@400;600&family=Montserrat:wght@700;800&family=Alex+Brush&display=swap" rel="stylesheet">
<style>
  :root {
    --stage: #ececec;
    --pouch-top: #7e2f18;
    --pouch-mid: #c4822a;
    --pouch-glow: #eebd4f;
    --pouch-low: #9c4c1c;
    --ink-brown: #5a2410;
    --band-brown: #5a1d10;
    --band-text: #f6c33a;
    --gold-light: #f4d27a;
    --shell-dark: #5a2810;
    --shell-mid: #8c4a22;
    --shell-light: #b06a36;
    --kernel-light: #f7dc92;
    --kernel-mid: #eab45a;
    --kernel-deep: #d08f34;
    --badge-light: #f6cf6c;
    --badge-deep: #c98424;
    --white: #ffffff;
  }
  * { margin: 0; padding: 0; box-sizing: border-box; }
  html, body { width: 1200px; height: 900px; overflow: hidden; background: var(--stage); }
  .canvas { position: relative; width: 1200px; height: 900px; background: var(--stage); }

  .pouch {
    position: absolute; left: 410px; top: 65px; width: 445px; height: 755px;
    border-radius: 4px; overflow: hidden;
    background:
      radial-gradient(ellipse 75% 40% at 50% 50%, var(--pouch-glow) 0%, rgba(238,189,79,0) 72%),
      linear-gradient(180deg, var(--pouch-top) 0%, #a8591f 18%, var(--pouch-mid) 40%, var(--pouch-mid) 62%, var(--pouch-low) 100%);
  }
  .seal-line { position: absolute; left: 0; right: 0; top: 82px; height: 2px; background: rgba(90,36,16,0.3); }

  .brand { position: absolute; left: 20px; top: 137px; display: flex; align-items: center; gap: 10px; }
  .brand-dot { width: 44px; height: 44px; border-radius: 50%; background: var(--band-text); }
  .brand-name {
    font-family: "Source Sans 3", sans-serif; font-weight: 400; font-size: 28px;
    color: var(--ink-brown); letter-spacing: 0.3px;
  }

  .free-badge { position: absolute; left: 310px; top: 122px; width: 94px; height: 94px; }
  .free-badge svg { position: absolute; inset: 0; }
  .free-badge-text {
    position: absolute; inset: 0; transform: rotate(-16deg);
    display: flex; flex-direction: column; align-items: center; justify-content: center;
    font-family: "Montserrat", sans-serif; color: var(--white); line-height: 1;
    text-shadow: 0 1px 2px rgba(90,36,16,0.7);
  }
  .free-badge-text .free { font-size: 19px; font-weight: 800; }
  .free-badge-text .cracker { font-size: 12px; font-weight: 700; margin-top: 3px; }

  .headline {
    position: absolute; left: 18px; top: 195px;
    font-family: "Source Sans 3", sans-serif; font-weight: 400; font-size: 68px;
    color: var(--ink-brown); line-height: 1;
  }
  .headline-script {
    position: absolute; left: 152px; top: 250px;
    font-family: "Alex Brush", cursive; font-size: 70px;
    color: var(--ink-brown); line-height: 1;
  }

  .product-band {
    position: absolute; left: 45px; top: 360px; width: 352px; height: 46px;
    border-radius: 8px; background: var(--band-brown);
    border: 2px solid rgba(244,210,122,0.55);
    display: flex; align-items: center; justify-content: center;
    font-family: "Montserrat", sans-serif; font-weight: 800; font-size: 19px;
    color: var(--band-text); letter-spacing: 0.3px;
  }

  .window {
    position: absolute; left: 62px; top: 420px; width: 320px; height: 320px;
    border-radius: 50%; border: 3px solid var(--gold-light);
    background:
      radial-gradient(circle at 45% 30%, var(--shell-light) 0%, rgba(176,106,54,0) 45%),
      radial-gradient(circle at 50% 45%, var(--shell-mid) 0%, var(--shell-dark) 80%);
    box-shadow: inset 0 6px 18px rgba(40,15,5,0.5);
  }

  .kernels { position: absolute; left: 0; right: 0; bottom: 0; height: 155px; }

  .net-weight {
    position: absolute; left: 143px; bottom: 0; width: 156px; height: 26px;
    border-radius: 6px 6px 0 0; background: var(--band-brown);
    display: flex; align-items: center; justify-content: center;
    font-family: "Source Sans 3", sans-serif; font-weight: 600; font-size: 15px;
    color: var(--white);
  }
</style>
</head>
<body>
<div class="canvas">
  <div class="pouch">
    <div class="seal-line"></div>

    <div class="brand">
      <span class="brand-dot"></span>
      <span class="brand-name">BRINDLECOVE</span>
    </div>

    <div class="free-badge">
      <svg width="94" height="94" viewBox="0 0 90 90" aria-hidden="true">
        <defs>
          <radialGradient id="badgeTone" cx="0.5" cy="0.45" r="0.6">
            <stop offset="0" stop-color="#f6cf6c"/>
            <stop offset="1" stop-color="#c98424"/>
          </radialGradient>
        </defs>
        <polygon fill="url(#badgeTone)" stroke="#fbe3a0" stroke-width="1.5"
          points="90,45 82.3,52.4 86.6,62.2 76.6,66.1 76.8,76.8 66.1,76.6 62.2,86.6 52.4,82.3 45,90 37.6,82.3 27.8,86.6 23.9,76.6 13.2,76.8 13.4,66.1 3.4,62.2 7.7,52.4 0,45 7.7,37.6 3.4,27.8 13.4,23.9 13.2,13.2 23.9,13.4 27.8,3.4 37.6,7.7 45,0 52.4,7.7 62.2,3.4 66.1,13.4 76.8,13.2 76.6,23.9 86.6,27.8 82.3,37.6"/>
      </svg>
      <div class="free-badge-text">
        <span class="free">FREE</span>
        <span class="cracker">Cracker!</span>
      </div>
    </div>

    <div class="headline">Indulge</div>
    <div class="headline-script">Yourself!</div>

    <div class="product-band">MACADEMIA NUTS IN SHELL</div>

    <div class="window" role="img" aria-label="Clear window showing macadamia nuts in their brown shells"></div>

    <svg class="kernels" width="445" height="155" viewBox="0 0 445 155" role="img" aria-label="Photograph of shelled golden macadamia kernels">
      <defs>
        <linearGradient id="kernelTone" x1="0" y1="0" x2="0" y2="1">
          <stop offset="0" stop-color="#f7dc92"/>
          <stop offset="0.55" stop-color="#eab45a"/>
          <stop offset="1" stop-color="#d08f34"/>
        </linearGradient>
      </defs>
      <path d="M0 45 Q30 20 70 32 Q120 12 170 30 Q205 8 245 22 Q290 10 330 28 Q380 14 445 30 L445 155 L0 155 Z" fill="url(#kernelTone)"/>
    </svg>

    <div class="net-weight">300 g | 10.58 oz</div>
  </div>
</div>
</body>
</html>
```